Business card and stationary for mobile ultrasound business
Brelintide Mobile Ultrasound
Business card and stationary for mobile ultrasound business - Medical
Professional
Tessa Quarrick
3817 W Larkfield Rd Ste D-415 Upland, CA 90254
info@brelintide.example
www.brelintide.example

```html
<!DOCTYPE html>
<html lang="en">
<head>
<meta charset="utf-8">
<title>Brelintide Mobile Ultrasound – Business Card</title>
<link href="https://fonts.googleapis.com/css2?family=Tinos:wght@400;700&display=swap" rel="stylesheet">
<style>
  :root {
    --bg: #e9eaec;
    --card: #fbfbfb;
    --teal: #2a8fae;
    --graphite: #4a4d50;
    --ink: #1e1e1e;
    --soft-line: #dcdcdc;
  }
  html, body {
    margin: 0;
    width: 1200px;
    height: 1000px;
    overflow: hidden;
    background: var(--bg);
  }
  .card {
    position: absolute;
    left: 100px;
    top: 210px;
    width: 1000px;
    height: 580px;
    background: var(--card);
    box-shadow: 0 10px 30px rgba(0,0,0,0.12);
    font-family: "Tinos", "Times New Roman", serif;
    color: var(--ink);
    overflow: hidden;
  }
  .card-shapes {
    position: absolute;
    inset: 0;
  }
  .brand {
    position: absolute;
    left: 62px;
    top: 44px;
    display: flex;
    align-items: center;
    gap: 16px;
  }
  .brand-dot {
    width: 22px;
    height: 22px;
    border-radius: 50%;
    background: var(--teal);
  }
  .brand-name {
    color: var(--teal);
    font-weight: 700;
    font-size: 38px;
    line-height: 1.05;
    letter-spacing: 2px;
    text-transform: uppercase;
  }
  .brand-name span { display: block; font-size: 24px; letter-spacing: 3px; }
  .person-name {
    position: absolute;
    left: 62px;
    top: 168px;
    margin: 0;
    color: var(--teal);
    font-weight: 700;
    font-size: 32px;
    letter-spacing: 1px;
    text-transform: uppercase;
  }
  .contact-list {
    position: absolute;
    left: 62px;
    top: 236px;
    margin: 0;
    padding: 0;
    list-style: none;
    font-size: 23px;
    line-height: 34px;
  }
  .contact-list li { display: flex; align-items: center; gap: 12px; }
  .contact-icon { width: 16px; height: 16px; flex: none; }
  .address {
    position: absolute;
    left: 62px;
    top: 412px;
    margin: 0;
    font-style: normal;
    font-size: 23px;
    line-height: 34px;
  }
</style>
</head>
<body>
  <section class="card">
    <svg class="card-shapes" width="1000" height="580" viewBox="0 0 1000 580">
      <polygon fill="var(--graphite)" points="690,210 790,150 790,390 690,440"/>
      <polygon fill="var(--soft-line)" points="800,145 830,132 830,580 800,580"/>
      <polygon fill="var(--teal)" points="840,128 1000,62 1000,500 930,580 840,580"/>
    </svg>

    <div class="brand">
      <div class="brand-dot"></div>
      <div class="brand-name">Brelintide<span>Mobile Ultrasound</span></div>
    </div>

    <h1 class="person-name">Tessa Quarrick</h1>

    <ul class="contact-list">
      <li>
        <svg class="contact-icon" viewBox="0 0 16 16"><rect width="16" height="16" rx="3" fill="var(--teal)"/><path d="M5 3.5h2l1 2.5-1.3 1a6 6 0 0 0 2.3 2.3l1-1.3 2.5 1v2a1 1 0 0 1-1 1A8 8 0 0 1 4 4.5a1 1 0 0 1 1-1z" fill="#fff"/></svg>
        (555) 204-7316
      </li>
      <li>
        <svg class="contact-icon" viewBox="0 0 16 16"><rect width="16" height="16" rx="3" fill="var(--teal)"/><rect x="5" y="2.5" width="6" height="11" rx="1.2" fill="#fff"/><rect x="6" y="4" width="4" height="7" fill="var(--teal)"/></svg>
        (555) 381-6042
      </li>
      <li>
        <svg class="contact-icon" viewBox="0 0 16 16"><rect width="16" height="16" rx="3" fill="var(--teal)"/><rect x="3" y="4.5" width="10" height="7" fill="#fff"/><path d="M3 4.5l5 4 5-4" fill="none" stroke="var(--teal)" stroke-width="1.2"/></svg>
        info@brelintide.example
      </li>
      <li>
        <svg class="contact-icon" viewBox="0 0 16 16"><circle cx="8" cy="8" r="8" fill="var(--teal)"/><circle cx="8" cy="8" r="5" fill="none" stroke="#fff" stroke-width="1.2"/><path d="M3 8h10M8 3c-2.5 3-2.5 7 0 10M8 3c2.5 3 2.5 7 0 10" fill="none" stroke="#fff" stroke-width="1"/></svg>
        www.brelintide.example
      </li>
    </ul>

    <address class="address">3817 W Larkfield Rd Ste D-415 Upland,<br>CA 90254</address>
  </section>
</body>
</html>
```